Acrylic print memorial plaque for entrance

I need a design for an acrylic print in DIN A0 portrait format or 1.5x DIN A0.

The top 40% should contain the lettering "Henrike's Pony Meadow." The lettering should frame three pictures. In the center is a portrait of Rike (Henrike), with "In Memoriam" below the name and the dates *November 20, 1980 †May 15, 2024. The head of the horse Pomelune should be placed on the left, and Belvina's head on the right.
The next 35% of the area should depict the portraits of Gustav (left), Jonte (middle), and Hedwig (right) in the upper part. Each with their name underneath. The lower part of this 35% should contain

“Our helpers:”
Then the portraits of Lennart, Franzi, Wiebke & Bernd should be taken in the following order. Each one should also have its name underneath the portrait.
The remaining 25% should contain the following:
“We would like to thank:
Ulrich & Gisela for their valuable support, and Hanni for her help and tips on handling the horse. We would also like to thank the Kramp family, especially Jupp & Hildegard and Basti & Svenja, for allowing us to create this paradise according to our ideas and for the construction. And, of course, the many other helpers and supporters.
The images should be isolated as much as possible and scaled to fit the print size. If possible, only the faces (head + neck) should be included.

Cut out, shape, or mirror the horse heads depending on the design.

The various images can be used as backgrounds, provided the design allows it.

Target Market(s)

No target mark, memorial plaque for the stable

Font styles to use
Serif
Decorative
Script

Requirements
Must have
• Honest, Authentic, Devotional
Should not have
• Kitsch, too playful.

```html
<!DOCTYPE html>
<html lang="de">
<head>
<meta charset="utf-8">
<title>Henrike's Pony Meadow – In Memoriam</title>
<link href="https://fonts.googleapis.com/css2?family=Dancing+Script:wght@700&family=Playfair+Display:ital,wght@1,700;1,800&family=Parisienne&family=Roboto+Condensed:wght@500&display=swap" rel="stylesheet">
<style>
  :root{
    --blue:#3b6894;
    --cream:#efe4d2;
    --white:#ffffff;
    --gold-light:#fbd895;
    --gold:#f0ae55;
    --gold-edge:#8a6a3c;
    --ink:#4e4a46;
    --plate-ink:#4a3d2e;
    --blossom:#efb3c6;
    --blossom-soft:#f5cdbd;
    --blossom-blue:#b9cfea;
    --peach:#f2b495;
  }
  *{margin:0;padding:0;box-sizing:border-box}
  html,body{width:848px;height:1200px;overflow:hidden;background:var(--cream)}
  .plaque{position:relative;width:848px;height:1200px;overflow:hidden}
  .backdrop{position:absolute;inset:0;
    background:linear-gradient(180deg,#f2e6d4 0%,#e8e0d3 30%,#dddcd6 55%,#e2ddd2 78%,#e9d7bd 100%)}
  .frame{position:absolute;inset:0}
  .title-text{font-family:'Dancing Script',cursive;font-weight:700;font-size:60px;fill:var(--white)}

  .ornament{position:absolute}
  .ornament.pink{border-radius:50%;background:linear-gradient(135deg,var(--blossom),var(--blossom-soft))}
  .ornament.blue{border-radius:50%;background:linear-gradient(135deg,var(--blossom-blue),#d7e3f2)}
  .ornament.peach{border-radius:50%;background:linear-gradient(135deg,var(--peach),#f7d0bd)}
  .ornament.strip{border-radius:24px;background:linear-gradient(180deg,#e6d3e6,#f2cdbf 60%,#e9a9bd)}

  .photo{position:absolute;overflow:hidden}
  .horse{top:206px;width:214px;height:214px;border-radius:50%;border:5px solid var(--white)}
  .horse-left{left:85px;background:linear-gradient(150deg,#9a9894 0%,#6f6b67 55%,#4a4643 100%)}
  .horse-right{left:549px;background:linear-gradient(210deg,#b4aca4 0%,#9a6a4b 50%,#8c4f2e 100%)}
  .portrait-main{left:289px;top:112px;width:272px;height:275px;border-radius:50% 50% 44% 44% / 52% 52% 40% 40%;
    border:7px solid var(--blue);background:linear-gradient(180deg,#e4e2de 0%,#cfb3a2 55%,#b88f7b 100%)}

  .memoriam{position:absolute;left:267px;top:377px;width:320px;height:52px;background:var(--blue);
    border-radius:26px 26px 0 0;color:var(--white);text-align:center;
    font-family:'Dancing Script',cursive;font-weight:700;font-size:37px;line-height:54px}
  .nameplate{position:absolute;left:295px;top:427px;width:260px;height:49px;border-radius:25px;
    border:2px solid var(--gold-edge);background:linear-gradient(180deg,var(--gold-light),var(--gold));
    text-align:center;color:var(--plate-ink)}
  .nameplate .name{font-family:'Playfair Display',serif;font-style:italic;font-weight:800;font-size:25px;line-height:28px;display:block;padding-top:2px}
  .nameplate .dates{font-family:'Roboto Condensed',sans-serif;font-weight:500;font-size:10px;display:block}

  .tile{position:absolute;border:4px solid var(--blue);background:var(--white);padding:4px}
  .tile .photo{position:relative;width:100%;height:100%}
  .family{top:501px;width:192px;height:162px}
  .helper{top:748px;width:151px;height:128px;border:none;padding:3px}
  .label{position:absolute;left:50%;transform:translateX(-50%);background:var(--blue);color:var(--white);
    border:3px solid var(--white);border-radius:18px;text-align:center;white-space:nowrap;
    font-family:'Playfair Display',serif;font-style:italic;font-weight:700}
  .family .label{bottom:-16px;width:134px;height:32px;font-size:17px;line-height:26px}
  .helper .label{bottom:-9px;width:112px;height:20px;background:var(--white);border:2px solid var(--blue);
    color:var(--blue);font-size:13px;line-height:16px}
  .tab{position:absolute;left:343px;top:701px;width:162px;height:31px;background:var(--blue);
    border-radius:10px 10px 0 0;color:var(--white);text-align:center;
    font-family:'Playfair Display',serif;font-style:italic;font-weight:700;font-size:16px;line-height:33px}
  .helpers-panel{position:absolute;left:85px;top:731px;width:677px;height:161px;background:var(--blue)}
  .thanks-head{position:absolute;left:272px;top:926px;width:303px;height:30px;background:var(--blue);
    border-radius:15px;color:var(--white);text-align:center;
    font-family:'Playfair Display',serif;font-style:italic;font-weight:700;font-size:17px;line-height:30px}
  .thanks{position:absolute;left:62px;top:970px;width:724px;text-align:center;color:var(--ink);
    font-family:'Parisienne',cursive;font-size:22.5px;line-height:29px}
</style>
</head>
<body>
<main class="plaque">
  <div class="backdrop" role="img" aria-label="Soft sky and sandy beach background with riders in the distance"></div>

  <svg class="frame" width="848" height="1200" viewBox="0 0 848 1200" aria-hidden="true">
    <path d="M24 140 V1180 H826 V165" fill="none" stroke="#3b6894" stroke-width="4"/>
    <path d="M24 98 Q424 -8 826 122 L826 178 Q424 42 24 150 Z" fill="#3b6894"/>
    <path id="titleLine" d="M24 134 Q424 30 826 160" fill="none"/>
    <text class="title-text" dy="18"><textPath href="#titleLine" startOffset="50%" text-anchor="middle">Henrike’s Pony Meadow</textPath></text>
  </svg>

  <div class="ornament pink" style="left:20px;top:22px;width:100px;height:100px" role="img" aria-label="Pink blossom ornament"></div>
  <div class="ornament pink" style="left:96px;top:20px;width:46px;height:46px" role="img" aria-label="Pink blossom ornament"></div>
  <div class="ornament blue" style="left:80px;top:120px;width:56px;height:56px" role="img" aria-label="Blue blossom ornament"></div>
  <div class="ornament peach" style="left:20px;top:135px;width:64px;height:66px" role="img" aria-label="Peach blossom ornament"></div>
  <div class="ornament pink" style="left:728px;top:55px;width:100px;height:100px" role="img" aria-label="Pink blossom ornament"></div>
  <div class="ornament pink" style="left:705px;top:20px;width:46px;height:46px" role="img" aria-label="Pink blossom ornament"></div>
  <div class="ornament blue" style="left:712px;top:122px;width:56px;height:56px" role="img" aria-label="Blue blossom ornament"></div>
  <div class="ornament peach" style="left:762px;top:140px;width:64px;height:66px" role="img" aria-label="Peach blossom ornament"></div>

  <div class="ornament strip" style="left:22px;top:990px;width:36px;height:120px" role="img" aria-label="Flower garland ornament"></div>
  <div class="ornament pink" style="left:28px;top:1106px;width:72px;height:68px" role="img" aria-label="Rose ornament"></div>
  <div class="ornament blue" style="left:120px;top:1130px;width:44px;height:40px" role="img" aria-label="Blue blossom ornament"></div>
  <div class="ornament strip" style="left:790px;top:990px;width:36px;height:120px" role="img" aria-label="Flower garland ornament"></div>
  <div class="ornament pink" style="left:748px;top:1106px;width:72px;height:68px" role="img" aria-label="Rose ornament"></div>
  <div class="ornament blue" style="left:684px;top:1130px;width:44px;height:40px" role="img" aria-label="Blue blossom ornament"></div>

  <div class="photo horse horse-left" role="img" aria-label="Head of the pony Pomelune"></div>
  <div class="photo horse horse-right" role="img" aria-label="Head of the horse Belvina"></div>
  <div class="photo portrait-main" role="img" aria-label="Portrait of Henrike"></div>

  <div class="memoriam">In Memoriam</div>
  <div class="ornament peach" style="left:216px;top:404px;width:86px;height:84px" role="img" aria-label="Flower ornament"></div>
  <div class="ornament peach" style="left:548px;top:404px;width:86px;height:84px" role="img" aria-label="Flower ornament"></div>
  <div class="nameplate"><span class="name">Henrike</span><span class="dates">20.11.1980 - † 15.05.2024</span></div>

  <div class="tile family" style="left:86px"><div class="photo" role="img" aria-label="Portrait of Gustav" style="background:linear-gradient(180deg,#8f8d86,#c9b5a6)"></div><span class="label">Gustav</span></div>
  <div class="tile family" style="left:328px"><div class="photo" role="img" aria-label="Portrait of Jonte" style="background:linear-gradient(180deg,#6e5f52,#c79e88)"></div><span class="label">Jonte</span></div>
  <div class="tile family" style="left:569px"><div class="photo" role="img" aria-label="Portrait of Hedwig" style="background:linear-gradient(180deg,#9fb0b8,#d3a791)"></div><span class="label">Hedwig</span></div>

  <div class="tab">Unsere Helfer</div>
  <div class="helpers-panel"></div>
  <div class="tile helper" style="left:102px"><div class="photo" role="img" aria-label="Portrait of Lennart" style="background:linear-gradient(180deg,#8fb2d0,#d2b59a)"></div><span class="label">Lennart</span></div>
  <div class="tile helper" style="left:267px"><div class="photo" role="img" aria-label="Portrait of Franzi" style="background:linear-gradient(180deg,#9cb6c6,#d0b89c)"></div><span class="label">Franzi</span></div>
  <div class="tile helper" style="left:431px"><div class="photo" role="img" aria-label="Portrait of Wiebke" style="background:linear-gradient(180deg,#94b3cc,#d4b99e)"></div><span class="label">Wiebke</span></div>
  <div class="tile helper" style="left:595px"><div class="photo" role="img" aria-label="Portrait of Bernd" style="background:linear-gradient(180deg,#9cbbd6,#a9b68e)"></div><span class="label">Bernd</span></div>

  <div class="thanks-head">Wir bedanken uns bei:</div>
  <p class="thanks">“Ulrich &amp; Gisela für die wertvolle Unterstützung, bei Hanni für die Hilfe und Tipps<br>im Umgang mit dem Pferd. Ebenfalls bedanken wir uns bei Familie Kramp,<br>vor allem bei Jupp &amp; Hildegard und Basti &amp; Svenja, dass wir dieses Paradies<br>nach unseren Vorstellungen schaffen durften und für die bauliche Umsetzung.<br>Und natürlich die vielen anderen Helfer und Trostspender.”</p>
</main>
</body>
</html>
```